Real Estate Website

The existing website design is http://brevanola.quillset4.com.au/ and we are not happy with it and need a fresh new design.

The menu of the website should be as it is however the content on the home page needs to include the following:

* Some sort of feature image/slideshow
* Introduction text and photo
* Our services section with boxes for 'strata management' 'property management' and 'property valuation & brokerage'. These boxes will then link to specific areas in the website
* Where are we with the contact details
* contact us with a form asking for name, email, phone, service interested in (as a dropdown) and comments box.
(do not include the who we are section)

In regards to design style/layout, here is what we like:
https://tarnelbeans.com/us/
https://www.coverlyne.com.au/
https://www.pendrake.com.au/
https://www.hqz.com/
https://www.vornelli.com.au/

```html
<!DOCTYPE html>
<html lang="en">
<head>
<meta charset="utf-8">
<title>Harwell &amp; Pike — Real Estate</title>
<link href="https://fonts.googleapis.com/css2?family=Cormorant+Garamond:wght@500;600;700&family=Roboto:wght@400;500;700&display=swap" rel="stylesheet">
<style>
:root{
  --navy:#2a358c;
  --navy-dark:#1f2870;
  --ink:#1c1d24;
  --text:#555a66;
  --pale:#eef2fb;
  --diamond:#e5e8f0;
  --white:#ffffff;
  --line:#d9dce4;
}
*{margin:0;padding:0;box-sizing:border-box}
html,body{width:1200px;height:4295px;overflow:hidden;background:var(--white)}
body{position:relative;font-family:"Roboto",sans-serif;color:var(--text)}
.abs{position:absolute}
.serif{font-family:"Cormorant Garamond",serif}
.btn{position:absolute;display:flex;align-items:center;justify-content:center;background:var(--navy);color:var(--white);font:700 14px "Roboto",sans-serif;letter-spacing:.2px;border-radius:2px}

/* hero */
.hero{position:absolute;left:0;top:0;width:1200px;height:682px;clip-path:polygon(0 0,100% 0,100% 567px,600px 678px,0 567px);
  background:linear-gradient(180deg,#5f86b8 0%,#8fb0cf 22%,#5d7f6a 40%,#7fa3c4 55%,#3f8fb0 70%,#c9b79e 85%,#e9e3da 100%)}
.hero-edge{position:absolute;left:0;top:560px}
.nav-logo{left:100px;top:22px;font:700 33px "Cormorant Garamond",serif;color:var(--white)}
.nav{left:412px;top:32px;display:flex;gap:0;font:500 13px "Roboto",sans-serif;color:var(--white)}
.nav span{margin-right:32px}
.login{left:944px;top:20px;width:156px;height:42px;background:var(--white);color:var(--navy);font:700 14px "Roboto",sans-serif;display:flex;align-items:center;justify-content:center;gap:6px;border-radius:2px}
.hero-kicker{left:100px;top:234px;font:400 25px "Roboto",sans-serif;color:var(--white)}
.hero-title{left:100px;top:274px;font:600 42px/46px "Cormorant Garamond",serif;color:var(--white)}
.arrow{top:322px;color:var(--white);font:300 34px "Roboto",sans-serif}

/* welcome */
.welcome-title{left:642px;top:775px;font:600 44px/50px "Cormorant Garamond",serif;color:var(--ink);letter-spacing:.5px}
.welcome-text{left:645px;top:893px;width:455px;font:400 14.5px/29px "Roboto",sans-serif;color:var(--text)}

/* offer */
.offer{position:absolute;left:0;top:1232px;width:1200px;height:1628px;background:var(--pale)}
.section-title{position:absolute;left:0;width:1200px;text-align:center;font:600 48px "Cormorant Garamond",serif;color:var(--ink)}
.section-sub{position:absolute;left:0;width:1200px;text-align:center;font:400 14.5px/27px "Roboto",sans-serif;color:#333}
.svc-title{font:700 27px "Roboto",sans-serif;color:var(--ink)}
.svc-text{width:470px;font:400 16px/26px "Roboto",sans-serif;color:var(--text)}
.svc-text p{margin-bottom:11px}
.photo{position:absolute}
.frame{position:absolute;background:var(--navy)}

/* where */
.where{position:absolute;left:0;top:2858px;width:1200px;height:527px;
  background:linear-gradient(90deg,#c7ccd3 0%,#d8dde3 30%,#e9ecef 60%,#f1eee9 100%)}
.where-title{left:720px;top:2922px;font:600 40px "Cormorant Garamond",serif;color:var(--ink)}
.where-row{position:absolute;left:722px;display:flex;gap:10px;font:400 17px/25px "Roboto",sans-serif;color:#222}

/* contact */
.field{position:absolute;border:1px solid var(--line);background:var(--white);font:400 15px "Roboto",sans-serif;color:#333;padding:12px 9px}
.map{position:absolute;left:625px;top:3600px;width:475px;height:295px;background:linear-gradient(135deg,#eceef2,#e2e5ea);box-shadow:0 4px 14px rgba(0,0,0,.18)}

/* footer */
.footer{position:absolute;left:0;top:3997px;width:1200px;height:298px;background:var(--navy)}
.foot-logo{left:98px;top:4060px;font:700 35px "Cormorant Garamond",serif;color:var(--white)}
.foot-head{font:700 16px "Roboto",sans-serif;color:var(--white)}
.foot-list{font:400 15px/28px "Roboto",sans-serif;color:var(--white)}
.copy{left:0;top:4252px;width:1200px;text-align:center;font:400 14px "Roboto",sans-serif;color:var(--white)}
</style>
</head>
<body>

<!-- Hero -->
<div class="hero" role="img" aria-label="Photo of a poolside terrace with white armchairs overlooking a lake and mountains"></div>
<svg class="hero-edge" width="1200" height="125" viewBox="0 0 1200 125">
  <polygon points="0,7 600,118 1200,7 1200,12 600,122 0,22" fill="var(--navy)"/>
</svg>
<div class="abs nav-logo">Harwell &amp; Pike</div>
<div class="abs nav"><span>HOME</span><span>ABOUT US</span><span>SERVICES</span><span>WHERE ARE WE</span><span>CONTACT US</span></div>
<div class="abs login">
  <svg width="14" height="14" viewBox="0 0 14 14"><path d="M1 6h7V3l4 4-4 4V8H1z" fill="var(--navy)"/><path d="M9 1h4v12H9" stroke="var(--navy)" stroke-width="1.6" fill="none"/></svg>
  CLIENT LOGIN</div>
<div class="abs hero-kicker">HARWELL &amp; PIKE</div>
<div class="abs hero-title">With 130 Years behind us,<br>we have a lot to offer</div>
<div class="btn" style="left:100px;top:393px;width:175px;height:42px;font-size:14.5px">GET STARTED NOW</div>
<div class="abs arrow" style="left:46px">&#8249;</div>
<div class="abs arrow" style="left:1132px">&#8250;</div>
<svg class="abs" style="left:589px;top:598px" width="22" height="32" viewBox="0 0 22 32"><rect x="1.5" y="1.5" width="19" height="29" rx="9.5" fill="none" stroke="#fff" stroke-width="2"/><line x1="11" y1="7" x2="11" y2="13" stroke="#fff" stroke-width="2"/></svg>

<!-- Welcome -->
<svg class="abs" style="left:20px;top:735px" width="570" height="420" viewBox="0 0 570 420">
  <g fill="var(--diamond)">
    <polygon points="210,5 305,100 210,195 115,100"/>
    <polygon points="95,115 190,210 95,305 0,210"/>
    <polygon points="210,225 305,320 210,415 115,320"/>
  </g>
  <polygon points="360,5 452,97 360,189 268,97" fill="#9aa6b6" role="img" aria-label="Photo of a modern two-storey house"/>
  <polygon points="275,95 367,187 275,279 183,187" fill="#a9a48f" role="img" aria-label="Photo of business people walking in a city"/>
  <polygon points="460,112 552,204 460,296 368,204" fill="#b8b7b3" role="img" aria-label="Photo of a smiling family at home"/>
  <polygon points="360,212 452,304 360,396 268,304" fill="#4f7fb8" role="img" aria-label="Photo of skyscrapers against a blue sky"/>
</svg>
<div class="abs welcome-title">WELCOME TO<br>HARWELL &amp; PIKE</div>
<div class="abs welcome-text">Harwell &amp; Pike was formed in 1888 by the then 20 year old J W Harwell, later to become Mayor of Ashmere. The company grew on the strength of its management department and the successful Auction of residential subdivisions in the developing suburbs of Ashmere, Linbrook, Westhaven and Corran Bay.</div>
<div class="btn" style="left:645px;top:1062px;width:144px;height:43px">LEARN MORE</div>

<!-- What we offer -->
<div class="offer"></div>
<div class="section-title" style="top:1305px">WHAT WE OFFER</div>
<div class="section-sub" style="top:1375px">Lorem ipsum dolor sit amet, consectetur adipiscing elit, sed do eiusmod<br>tempor incididunt ut labore et dolore magna aliqua</div>

<!-- Strata -->
<svg class="abs" style="left:103px;top:1455px" width="76" height="76" viewBox="0 0 76 76" fill="none" stroke="var(--navy)" stroke-width="2.4">
  <circle cx="38" cy="22" r="18"/><circle cx="38" cy="19" r="5"/><path d="M29 33c2-6 16-6 18 0"/>
  <path d="M4 48l16-8 14 6 10 0-2 6-14 0"/><path d="M72 48l-16-8-10 6"/><path d="M20 58l14 10 12-4 22-14"/>
</svg>
<div class="abs svc-title" style="left:98px;top:1543px">Strata Management</div>
<div class="abs svc-text" style="left:98px;top:1597px"><p>Nervous about your property adventure? Don't be. Whether you're getting ready to buy or sell, in the middle of it, or just looking for some answers, our top-notch skills ensure you get the best experience possible.</p><p>It's what we love to do.</p></div>
<div class="btn" style="left:98px;top:1768px;width:144px;height:43px">LEARN MORE</div>
<div class="frame" style="left:900px;top:1443px;width:200px;height:12px"></div>
<div class="frame" style="left:1088px;top:1443px;width:12px;height:180px"></div>
<div class="photo" style="left:630px;top:1457px;width:457px;height:368px;background:linear-gradient(135deg,#b39a78,#d8cbb7 55%,#8f8a85)" role="img" aria-label="Photo of three young people reviewing documents at a table"></div>

<!-- Property management -->
<div class="frame" style="left:100px;top:1918px;width:200px;height:12px"></div>
<div class="frame" style="left:100px;top:1918px;width:12px;height:180px"></div>
<div class="photo" style="left:113px;top:1932px;width:457px;height:368px;background:linear-gradient(135deg,#e7e2d8,#cfc5b5 50%,#8a7d6f)" role="img" aria-label="Photo of two men discussing house plans at a desk"></div>
<svg class="abs" style="left:628px;top:1930px" width="72" height="72" viewBox="0 0 72 72" fill="none" stroke="var(--navy)" stroke-width="2.4">
  <rect x="18" y="4" width="40" height="30"/><path d="M24 12h8M44 12h8M24 22h8M44 22h8"/>
  <path d="M4 44h16l10 4h14v6H28"/><path d="M4 66h20l26-8 18-12-6-4-18 10"/><rect x="2" y="42" width="6" height="26"/>
</svg>
<div class="abs svc-title" style="left:628px;top:2018px">Property Management</div>
<div class="abs svc-text" style="left:628px;top:2072px"><p>Large or small, condo or mansion, we can find it and get it for you at the price that's right. TICs? Fixer-uppers? Luxury?</p><p>We can help with all of it. We always have a current list of available properties for you to check out.</p></div>
<div class="btn" style="left:628px;top:2243px;width:144px;height:43px">LEARN MORE</div>

<!-- Valuation -->
<svg class="abs" style="left:98px;top:2390px" width="86" height="84" viewBox="0 0 86 84" fill="none" stroke="var(--navy)" stroke-width="2.4">
  <circle cx="18" cy="18" r="15"/><path d="M22 12c-3-3-10-2-9 3s10 2 9 7-7 5-10 2M18 8v4M18 24v4"/>
  <rect x="46" y="20" width="24" height="62"/><path d="M52 4v16M58 10v10M50 30h16M50 40h16M50 50h16M50 60h16"/>
  <rect x="32" y="42" width="14" height="40"/><path d="M2 82h84M10 60v22M18 68v14"/>
</svg>
<div class="abs svc-title" style="left:98px;top:2483px">Property Valuation &amp; Brokerage</div>
<div class="abs svc-text" style="left:98px;top:2537px"><p>If you have questions about affordability, credit, legal matters, or income, trust us to find you what you need fast.</p><p>We make sure you feel confident and educated every step of the way.</p></div>
<div class="btn" style="left:98px;top:2708px;width:144px;height:43px">LEARN MORE</div>
<div class="frame" style="left:900px;top:2383px;width:200px;height:12px"></div>
<div class="frame" style="left:1088px;top:2383px;width:12px;height:180px"></div>
<div class="photo" style="left:630px;top:2397px;width:457px;height:368px;background:linear-gradient(135deg,#44464d,#9ea3a8 55%,#f1efec)" role="img" aria-label="Photo of a person using a calculator beside a small model house"></div>

<!-- Where are we -->
<div class="where" role="img" aria-label="Photo of a happy couple holding house keys in a new home with moving boxes"></div>
<div class="abs where-title">WHERE ARE WE</div>
<div class="where-row" style="top:2983px">
  <svg width="16" height="22" viewBox="0 0 16 22"><path d="M8 1a7 7 0 0 1 7 7c0 5-7 13-7 13S1 13 1 8a7 7 0 0 1 7-7z" fill="var(--navy)"/><circle cx="8" cy="8" r="2.6" fill="#fff"/></svg>
  <div>Harwell &amp; Pike<br>48 Larkspur Road, Westhaven<br>New South Wales 2099, Australia</div>
</div>
<div class="where-row" style="top:3083px">
  <svg width="16" height="22" viewBox="0 0 16 16"><path d="M3 1l3 1 1 4-2 1c1 3 3 5 6 6l1-2 4 1 1 3-2 1C8 16 0 8 1 3z" fill="var(--navy)"/></svg>
  <div>(02) 9000 4127<br>reception@harwellpike.com.au<br>accounts@harwellpike.com.au</div>
</div>
<svg class="abs" style="left:722px;top:3118px" width="16" height="12" viewBox="0 0 16 12"><rect width="16" height="12" fill="var(--navy)"/><path d="M0 0l8 7 8-7" stroke="#fff" stroke-width="1.4" fill="none"/></svg>
<svg class="abs" style="left:722px;top:3143px" width="16" height="12" viewBox="0 0 16 12"><rect width="16" height="12" fill="var(--navy)"/><path d="M0 0l8 7 8-7" stroke="#fff" stroke-width="1.4" fill="none"/></svg>
<div class="where-row" style="top:3182px">
  <svg width="16" height="22" viewBox="0 0 16 16"><circle cx="8" cy="8" r="8" fill="var(--navy)"/><path d="M8 3v5l3 2" stroke="#fff" stroke-width="1.6" fill="none"/></svg>
  <div>Mon - Fri 9:00 am - 5:00 pm<br>Sat - 10:00 am &ndash; 04:00 pm<br>Sun - Closed</div>
</div>
<div class="btn" style="left:721px;top:3274px;width:157px;height:43px">DROP US A LINE</div>

<!-- Contact -->
<div class="section-title" style="top:3483px;font-size:50px">CONTACT US</div>
<div class="section-sub" style="top:3545px;font-size:16px">Fill out your information below, we will give you a call shortly.</div>
<div class="field" style="left:100px;top:3603px;width:241px;height:41px">Full Name*</div>
<div class="field" style="left:349px;top:3603px;width:241px;height:41px">Phone*</div>
<div class="field" style="left:100px;top:3653px;width:241px;height:41px">Email*</div>
<div class="field" style="left:349px;top:3653px;width:241px;height:41px">Services*
  <svg style="position:absolute;right:12px;top:17px" width="8" height="5" viewBox="0 0 8 5"><path d="M0 0h8L4 5z" fill="#333"/></svg></div>
<div class="field" style="left:100px;top:3703px;width:490px;height:138px">Your Message*</div>
<div class="btn" style="left:263px;top:3851px;width:163px;height:45px;gap:8px;font-size:15px;letter-spacing:.5px">SUBMIT NOW
  <svg width="16" height="14" viewBox="0 0 16 14"><path d="M0 6L16 0 12 14 8 9 14 2 6 8z" fill="#fff"/></svg></div>
<div class="map" role="img" aria-label="Street map showing the office location with a marker"></div>

<!-- Footer -->
<div class="footer"></div>
<div class="abs foot-logo">Harwell &amp; Pike</div>
<svg class="abs" style="left:96px;top:4120px" width="114" height="34" viewBox="0 0 114 34" fill="none" stroke="#fff" stroke-width="1.5">
  <circle cx="17" cy="17" r="15"/><circle cx="56" cy="17" r="15"/><circle cx="96" cy="17" r="15"/>
</svg>
<div class="abs foot-head" style="left:380px;top:4068px">ABOUT</div>
<div class="abs foot-list" style="left:380px;top:4103px">&gt;&gt;&nbsp; Company<br>&gt;&gt;&nbsp; Our Team<br>&gt;&gt;&nbsp; Our Services</div>
<div class="abs foot-head" style="left:580px;top:4068px">LINKS</div>
<div class="abs foot-list" style="left:580px;top:4103px">&gt;&gt;&nbsp; Appraisal Request<br>&gt;&gt;&nbsp; Tenant Application<br>&gt;&gt;&nbsp; Maintenance Request</div>
<div class="abs foot-head" style="left:848px;top:4068px">SUBSCRIBE FOR NEWSLATTER</div>
<div class="field" style="left:845px;top:4097px;width:253px;height:40px;border:none;border-radius:3px;font-size:13px;color:#666">Email Address</div>
<div class="btn" style="left:845px;top:4148px;width:253px;height:40px;background:#1b1c2a;border-radius:3px">SUBMIT</div>
<div class="abs" style="left:100px;top:4225px;width:1000px;height:1px;background:rgba(255,255,255,.35)"></div>
<div class="abs copy">&copy; 2021 Harwell &amp; Pike. All Rights Reserved.&nbsp;&nbsp;&nbsp;Disclaimer&nbsp;&nbsp;&nbsp;&nbsp;|&nbsp;&nbsp;&nbsp;&nbsp;Privacy</div>
<svg class="abs" style="left:1142px;top:4235px" width="46" height="46" viewBox="0 0 46 46"><circle cx="23" cy="23" r="22" fill="#fff"/><path d="M15 27l8-8 8 8" stroke="var(--navy)" stroke-width="2" fill="none"/></svg>

</body>
</html>
```